TBNW site redesign

Please redesign a home page with content provided. PSD only - no coding
Can use any images from Vexelmarq.com

Please create a site design that more clearly illustrates the client's services and expertise. We are looking for a high-end design.

Any images used must be generic or of Dallas TX.

Fonts: Any
Colors: Match to logo
Look: Modern - Professional

Target Market(s)

medium-large business owners

Number of Pages Required

1 page

Font styles to use
Serif
Sans Serif

Requirements
Must have
• cohesive professional design
• high end look
• Match to logo

```html
<!DOCTYPE html>
<html lang="en">
<head>
<meta charset="utf-8">
<title>TBNW | Professional Office and Warehouse Leasing</title>
<link rel="stylesheet" href="https://fonts.googleapis.com/css2?family=Work+Sans:wght@400;500;600;700&display=swap">
<style>
:root{
  --red:#d73a35;
  --red-dark:#b82d29;
  --ink:#2b2b2b;
  --text:#555;
  --muted:#888;
  --light:#f3f3f3;
  --white:#fff;
  --hero-a:#3a2418;
  --hero-b:#a8603a;
  --band-a:#2a1714;
  --band-b:#6a3a30;
}
*{margin:0;padding:0;box-sizing:border-box}
html,body{width:1200px;height:3315px;overflow:hidden}
body{font-family:"Work Sans",Arial,sans-serif;color:var(--text);background:var(--white);position:relative}
.abs{position:absolute}
.btn{position:absolute;display:flex;align-items:center;justify-content:center;background:var(--red);color:var(--white);font-weight:600;font-size:15px;letter-spacing:1.5px;text-transform:uppercase}
.btn-outline{background:var(--white);color:var(--ink);border:2px solid #999}

/* header */
.site-header{position:absolute;left:0;top:0;width:1200px;height:110px;background:var(--white)}
.brand{position:absolute;left:96px;top:20px;display:flex;align-items:center;gap:12px}
.brand-mark{width:30px;height:30px;background:var(--red)}
.brand-name{font-size:30px;font-weight:700;color:var(--ink);letter-spacing:2px}
.brand-sub{position:absolute;left:96px;top:62px;font-size:11px;letter-spacing:2px;color:var(--ink);text-transform:uppercase}
.social{position:absolute;left:706px;top:22px;display:flex;gap:10px}
.social span{width:13px;height:13px;border-radius:50%;background:var(--ink)}
.social span:first-child{background:var(--red)}
.call{position:absolute;left:848px;top:18px;font-size:13px;letter-spacing:1.5px;color:var(--ink)}
.call b{font-size:21px;font-weight:500;color:var(--red);letter-spacing:1px;margin-left:8px}
.nav{position:absolute;right:84px;top:76px;display:flex;gap:36px;font-size:13px;font-weight:500;letter-spacing:1.3px;color:var(--ink)}
.nav .active{position:relative}
.nav .active::before{content:"";position:absolute;left:0;right:0;top:-14px;height:3px;background:var(--red)}

/* hero */
.hero{position:absolute;left:0;top:110px;width:1200px;height:490px;background:linear-gradient(180deg,#c58a5a 0%,var(--hero-b) 30%,var(--hero-a) 100%)}
.hero h1{position:absolute;left:84px;top:172px;font-size:42px;line-height:48px;font-weight:700;color:var(--white);letter-spacing:1.5px}
.hero p{position:absolute;left:84px;top:268px;width:600px;font-size:16px;line-height:22px;color:var(--white);font-weight:500}
.arrow{position:absolute;top:228px}

/* about */
.eyebrow{position:absolute;width:1200px;text-align:center;font-size:14px;letter-spacing:1.5px;color:var(--ink)}
.section-title{position:absolute;width:1200px;text-align:center;font-size:32px;font-weight:400;letter-spacing:1.5px;color:var(--ink)}
.about-copy{position:absolute;left:88px;top:734px;width:1024px;font-size:13.5px;line-height:20.5px;text-align:center;color:var(--text)}

/* why */
.why{position:absolute;left:0;top:940px;width:1200px;height:347px;background:linear-gradient(180deg,var(--band-a),var(--band-b) 60%,#8a4c3a)}
.why h2{position:absolute;width:1200px;top:52px;text-align:center;font-size:30px;font-weight:400;letter-spacing:2px;color:var(--white)}
.cards{position:absolute;left:88px;top:125px;width:1026px;height:222px;display:flex;box-shadow:0 6px 18px rgba(0,0,0,.25)}
.card{flex:1;background:var(--red);padding:20px 24px;color:var(--white)}
.card:nth-child(2),.card:nth-child(4){background:var(--red-dark)}
.card-head{display:flex;align-items:center;gap:14px;height:42px}
.card-head h3{font-size:16px;font-weight:600;letter-spacing:1.5px;line-height:18px}
.card p{margin-top:16px;font-size:13px;line-height:20px}

/* team */
.team-copy{position:absolute;left:88px;top:1390px;width:1024px;font-size:13.5px;line-height:22px;text-align:center}
.member{position:absolute;top:1474px;width:239px;text-align:center}
.portrait{width:239px;height:276px;background:linear-gradient(180deg,#e6e6e6,#cfcfcf 55%,#3b4656 100%)}
.member h4{margin-top:13px;font-size:17px;font-weight:400;color:var(--red)}
.member p{margin-top:6px;font-size:12.5px;line-height:18px;color:var(--ink)}

/* cta */
.cta{position:absolute;left:0;top:1885px;width:1200px;height:192px;background:linear-gradient(90deg,#3a1412,#5a1d1a 50%,#2a1212)}
.cta p{position:absolute;left:80px;top:42px;width:1040px;text-align:center;font-size:21px;line-height:29px;color:var(--white);letter-spacing:.5px}

/* testimonials */
.testimonials{position:absolute;left:0;top:2077px;width:1200px;height:350px;background:linear-gradient(180deg,#ece9ec 0%,#e9dfe0 55%,#eec9a8 100%)}
.quote-mark{position:absolute;left:577px;top:112px}
.quote{position:absolute;left:84px;top:148px;width:1032px;text-align:center;font-size:13.5px;line-height:21px;color:var(--ink)}
.quote-name{position:absolute;width:1200px;top:232px;text-align:center;font-size:13px;font-weight:600;color:var(--ink)}
.dots{position:absolute;left:580px;top:276px;display:flex;gap:5px}
.dots span{width:10px;height:10px;border-radius:50%;background:#bbb}
.dots span:first-child{background:var(--red)}

/* articles */
.article{position:absolute;top:2541px;width:326px;height:469px;background:var(--light);box-shadow:0 2px 6px rgba(0,0,0,.12)}
.article-img{position:relative;height:217px}
.article-date{position:absolute;left:0;bottom:0;padding:5px 8px;background:rgba(0,0,0,.55);color:var(--white);font-size:12px}
.article h4{padding:22px 14px 0;font-size:16.5px;line-height:21px;font-weight:400;color:var(--red)}
.article p{padding:12px 14px 0;font-size:12.5px;line-height:19px;color:var(--text);height:110px;overflow:hidden}
.article .btn{left:16px;top:405px;width:294px;height:38px}

/* footer */
.site-footer{position:absolute;left:0;top:3072px;width:1200px;height:243px;background:var(--red);color:var(--white)}
.footer-brand{position:absolute;left:84px;top:44px;width:177px;height:77px;background:var(--white);display:flex;flex-direction:column;align-items:center;justify-content:center;gap:4px}
.footer-brand .brand-name{font-size:22px}
.footer-brand small{font-size:8px;letter-spacing:1.3px;color:var(--ink);text-transform:uppercase}
.disclosure{position:absolute;left:350px;top:42px;width:480px}
.disclosure h5{font-size:13px;font-weight:600;line-height:18px}
.disclosure ul{list-style:none;margin-top:12px}
.disclosure li{font-size:12.5px;line-height:23px;text-decoration:underline}
.disclosure li::before{content:"» ";text-decoration:none;display:inline-block;margin-right:4px}
.contact{position:absolute;left:895px;top:42px;width:240px}
.contact h5{font-size:13px;font-weight:600}
.contact .row{display:flex;gap:12px;margin-top:12px;font-size:12px;line-height:17px}
.footer-social{position:absolute;left:895px;top:200px;display:flex;gap:10px}
.footer-social span{width:12px;height:12px;border-radius:50%;background:var(--white)}
.copyright{position:absolute;left:84px;top:208px;font-size:12px}
</style>
</head>
<body>

<header class="site-header">
  <div class="brand"><span class="brand-mark"></span><span class="brand-name">TBNW</span></div>
  <div class="brand-sub">Brannock Wells Realty Group</div>
  <div class="social" aria-label="Social links"><span></span><span></span><span></span><span></span></div>
  <div class="call">CALL TODAY: <b>214-555-0142</b></div>
  <nav class="nav"><span class="active">HOME</span><span>ABOUT TBNW</span><span>CONTACT US</span><span>BLOG</span><span>MARKET NEWS</span></nav>
</header>

<section class="hero" role="img" aria-label="Dallas skyline at sunset with downtown office towers">
  <svg class="arrow" style="left:26px" width="16" height="30" viewBox="0 0 16 30"><path d="M14 2 2 15l12 13" stroke="#fff" stroke-width="2.5" fill="none"/></svg>
  <svg class="arrow" style="right:26px" width="16" height="30" viewBox="0 0 16 30"><path d="m2 2 12 13L2 28" stroke="#fff" stroke-width="2.5" fill="none"/></svg>
  <h1>PROFESSIONAL OFFICE AND<br>WAREHOUSE LEASING</h1>
  <p>Fast-track your search with tenant reps that only serve you, and specialize in the DFW area.</p>
</section>

<section class="about">
  <div class="eyebrow" style="top:657px">ABOUT TBNW</div>
  <h2 class="section-title" style="top:686px">LET US HANDLE YOUR COMMERCIAL REAL ESTATE LEASE</h2>
  <p class="about-copy">Lorem Ipsum is simply dummy text of the printing and typesetting industry. Lorem Ipsum has been the industry's standard dummy text ever since the 1500s, when an unknown printer took a galley of type and scrambled it to make a type specimen book. It has survived not only five centuries, but also the leap into electronic typesetting, remaining essentially unchanged. It was popularised in the 1960s with the release of Typeset sheets containing Lorem Ipsum passages, and more recently with desktop publishing software like Folio Layout including versions of Lorem Ipsum.</p>
  <div class="btn" style="left:457px;top:838px;width:286px;height:37px">READ MORE</div>
</section>

<section class="why" role="img" aria-label="Dusk view of a stadium and city lights">
  <h2>WHY TENANT REPRESENTATION?</h2>
  <div class="cards">
    <div class="card">
      <div class="card-head"><svg width="32" height="30" viewBox="0 0 32 30"><circle cx="16" cy="7" r="5" fill="#fff"/><circle cx="6" cy="22" r="5" fill="#fff"/><circle cx="26" cy="22" r="5" fill="#fff"/><path d="M16 12v5M10 20l6-3 6 3" stroke="#fff" stroke-width="2" fill="none"/></svg><h3>RELATIONSHIPS</h3></div>
      <p>Save time by trusting TBNW year after year to find the right location for you. Once we've worked together, we know what you need, and you can keep your budget details private.</p>
    </div>
    <div class="card">
      <div class="card-head"><svg width="24" height="34" viewBox="0 0 24 34"><rect x="3" y="2" width="18" height="30" rx="2" fill="none" stroke="#fff" stroke-width="2.5"/><rect x="8" y="14" width="10" height="4" fill="#fff"/></svg><h3>ACCESS TO<br>MORE</h3></div>
      <p>We have no agreements or personal incentives for specific properties, so we can always show you the offices that are right for you.</p>
    </div>
    <div class="card">
      <div class="card-head"><svg width="34" height="24" viewBox="0 0 34 24"><rect x="1" y="1" width="32" height="22" rx="3" fill="#fff"/><rect x="6" y="9" width="22" height="6" fill="#d73a35"/></svg><h3>FREE TO YOU</h3></div>
      <p>You pay us nothing. We get our commission from the property being leased.</p>
    </div>
    <div class="card">
      <div class="card-head"><svg width="32" height="32" viewBox="0 0 32 32"><circle cx="16" cy="16" r="11" fill="none" stroke="#fff" stroke-width="6" stroke-dasharray="5 3"/><circle cx="16" cy="16" r="5" fill="#fff"/></svg><h3>CUSTOMIZED<br>SERVICE</h3></div>
      <p>Aside from saving you the time of repeating what your needs are to each new location, we also provide a report of the places you've seen, so it's easier to share and make a decision.</p>
    </div>
  </div>
</section>

<section class="team">
  <h2 class="section-title" style="top:1338px">MEET THE TEAM</h2>
  <p class="team-copy">At TBNW we believe that you deserve the best professional advice and personal service with your commercial real estate negotiations. By choosing TBNW as your tenant reps in the Dallas/Fort Worth area, you will receive the assistance of accomplished and experienced commercial real estate brokers and salespeople who are licensed by the State Realty Licensing Board to practice in Texas since 1983.</p>
  <div class="member" style="left:128px"><div class="portrait" role="img" aria-label="Portrait of the founder in a suit"></div><h4>Warren J. Brannock</h4><p>- Founder and President</p></div>
  <div class="member" style="left:482px"><div class="portrait" role="img" aria-label="Portrait of the senior director in a suit"></div><h4>Owen Castellano</h4><p>- Senior Director, Commercial<br>Property Specialist</p></div>
  <div class="member" style="left:833px"><div class="portrait" role="img" aria-label="Portrait of the associate in a suit"></div><h4>Dylan Reese Harlow</h4><p>- Jr., Associate, Tenant Rep Specialist</p></div>
</section>

<section class="cta" role="img" aria-label="Desk with calculator and documents in low light">
  <p>If you need to find office or warehouse space in the Dallas Fort Worth area, the team at TBNW has the experience you need.</p>
  <div class="btn" style="left:457px;top:113px;width:286px;height:35px;font-size:14px">SPACE CALCULATOR</div>
</section>

<section class="testimonials" role="img" aria-label="Soft view of a cable bridge at sunrise">
  <h2 class="section-title" style="top:50px">CLIENT TESTIMONIALS</h2>
  <svg class="quote-mark" width="46" height="34" viewBox="0 0 46 34"><path d="M0 34V18C0 8 6 2 16 0l2 5c-6 2-8 6-8 11h8v18zM26 34V18c0-10 6-16 16-18l2 5c-6 2-8 6-8 11h8v18z" fill="#d73a35"/></svg>
  <p class="quote">"The real estate team at TBNW has decades of experience in Commercial. One advantage of TBNW is they know all the properties that are about to becomeavailable, BEFORE they are available. They have the inside track on properties and they watch your back at the negotiating table. Very impressive with a polished approach. Let the team run with your next project and you won't be disappointed."</p>
  <div class="quote-name">Nathan Ellis Crane</div>
  <div class="dots"><span></span><span></span><span></span></div>
</section>

<section class="articles">
  <h2 class="section-title" style="top:2476px">RECENT ARTICLES</h2>
  <article class="article" style="left:88px">
    <div class="article-img" role="img" aria-label="Bright open-plan office interior" style="background:linear-gradient(180deg,#d9dde0,#a9b0b6)"><span class="article-date">20th Apr, 2018</span></div>
    <h4>Do You Need Office Space? Don't Miss These Flexible Options!</h4>
    <p>If your company needs office space now but isn't ready for a long-term office lease, are there any options? Actually, there are. Local office space services find that there are quite a few flexible rental options available if you know where to look.</p>
    <div class="btn btn-outline">READ MORE</div>
  </article>
  <article class="article" style="left:437px">
    <div class="article-img" role="img" aria-label="Sunlit shared workspace with people walking" style="background:linear-gradient(180deg,#e8c690,#8a6440)"><span class="article-date">14th Feb, 2018</span></div>
    <h4>Shared Building Amenities – Is Your Office Space Growing?</h4>
    <p>When searching for a building to lease for your company, one important detail to consider is space, both usable and rentable. Office space in multi-tenant buildings includes both types of space, each of which can be used by your team.</p>
    <div class="btn btn-outline">READ MORE</div>
  </article>
  <article class="article" style="left:789px">
    <div class="article-img" role="img" aria-label="Modern stone and glass commercial building" style="background:linear-gradient(180deg,#8fb6d8 0%,#a8c4dc 40%,#7a5a44 70%,#6a6a6a 100%)"><span class="article-date">11th Jan, 2018</span></div>
    <h4>Commercial Tenant Due Diligence When Considering Relocation!</h4>
    <p>When a tenant relocates to new commercial real estate property, it is their responsibility to perform due diligence prior to signing the lease agreement. Because this process can be time-consuming and requires a thorough review.</p>
    <div class="btn btn-outline">READ MORE</div>
  </article>
</section>

<footer class="site-footer">
  <div class="footer-brand"><div class="brand" style="position:static;gap:8px"><span class="brand-mark" style="width:22px;height:22px"></span><span class="brand-name">TBNW</span></div><small>Brannock Wells Realty Group</small></div>
  <div class="disclosure">
    <h5>State Realty Licensing Board Mandated Disclosure Notices<br>– click links below to view pages</h5>
    <ul><li>State Realty Licensing Board Information About Brokerage Services</li><li>State Realty Licensing Board Consumer Protection Notice</li></ul>
  </div>
  <div class="contact">
    <h5>Contact Info</h5>
    <div class="row"><svg width="12" height="16" viewBox="0 0 12 16"><path d="M6 0a6 6 0 0 0-6 6c0 4 6 10 6 10s6-6 6-10a6 6 0 0 0-6-6z" fill="#fff"/><circle cx="6" cy="6" r="2" fill="#d73a35"/></svg><span>410 Cedar Row Avenue, Suite 300,<br>Dallas, TX 75201</span></div>
    <div class="row"><svg width="12" height="14" viewBox="0 0 12 14"><path d="M2 0h3l1 4-2 1c1 2 2 3 4 4l1-2 3 1v3c0 1-1 2-2 2C5 13 0 8 0 2 0 1 1 0 2 0z" fill="#fff"/></svg><span>214-555-0142</span></div>
    <div class="row"><svg width="14" height="14" viewBox="0 0 14 14"><rect x="1" y="4" width="12" height="9" fill="#fff"/><rect x="3" y="0" width="8" height="5" fill="#fff"/><rect x="3" y="7" width="8" height="2" fill="#d73a35"/></svg><span>214-555-0187</span></div>
  </div>
  <div class="footer-social" aria-label="Social links"><span></span><span></span><span></span><span></span></div>
  <svg class="abs" style="left:1086px;top:200px" width="26" height="16" viewBox="0 0 26 16"><path d="M2 14 13 3l11 11" stroke="#fff" stroke-width="4" fill="none"/></svg>
  <div class="copyright">Copyright © 2018 &nbsp;|&nbsp; All Rights Reserved.</div>
</footer>

</body>
</html>
```